redesing professional certificate

Redesign our certificate to more a professional look and to make it look like a-wanna have - Best in adobe photoshop, because this template will be our basic, and we have in our education different levels, basic, upper, lower, complex, master level. I usually add a small picture to show what level they are. Or when you have a better suggestion I a gladly to hear.
We teach to physiotherapist so it has to look professional.

Target Market(s)

physiotherapist

Industry/Entity Type

Health Care

Requirements
Must have
• our logo

```html
<!DOCTYPE html>
<html lang="en">
<head>
<meta charset="utf-8">
<title>Certificate of Achievement</title>
<link rel="stylesheet" href="https://fonts.googleapis.com/css2?family=Montserrat:wght@400;500;700;900&family=Great+Vibes&family=Open+Sans:wght@400;700&display=swap">
<style>
  :root {
    --navy: #15233f;
    --ink: #2b2f36;
    --ribbon: #1d5a86;
    --ribbon-tail: #153f60;
    --band: #0b5b98;
    --blue-deep: #0d3fa8;
    --blue-bright: #2f7de1;
    --silver-light: #f1f3f6;
    --silver-dark: #b9c0ca;
    --paper: #ffffff;
  }
  * { margin: 0; padding: 0; box-sizing: border-box; }
  html, body { width: 1200px; height: 979px; overflow: hidden; background: var(--paper); }
  .certificate {
    position: relative; width: 1200px; height: 979px;
    background: var(--paper); font-family: "Montserrat", sans-serif; color: var(--ink);
  }
  .corner-art { position: absolute; left: 0; top: 0; width: 420px; height: 660px; }
  .brand {
    position: absolute; right: 60px; top: 72px;
    display: flex; align-items: center; gap: 12px;
    font-family: "Montserrat", sans-serif; font-weight: 700; font-size: 24px;
    color: var(--navy); letter-spacing: 1px;
  }
  .brand-dot { width: 22px; height: 22px; border-radius: 50%; background: var(--navy); }
  .title {
    position: absolute; left: 0; right: 0; top: 190px; text-align: center;
    font-weight: 900; font-size: 104px; line-height: 1; color: var(--navy); letter-spacing: 1px;
  }
  .subtitle {
    position: absolute; left: 0; right: 0; top: 312px; text-align: center;
    font-weight: 500; font-size: 27px; letter-spacing: 2px; color: var(--navy);
  }
  .ribbon { position: absolute; left: 316px; top: 358px; width: 571px; height: 52px; }
  .ribbon-text {
    position: absolute; left: 361px; top: 358px; width: 482px; height: 46px;
    display: flex; align-items: center; justify-content: center;
    color: #fff; font-size: 22px; font-weight: 500;
  }
  .recipient {
    position: absolute; left: 0; right: 0; top: 430px; text-align: center;
    font-family: "Great Vibes", cursive; font-size: 84px; line-height: 1; color: var(--navy);
  }
  .recipient-line { position: absolute; left: 336px; top: 527px; width: 531px; height: 1px; background: var(--navy); }
  .details {
    position: absolute; left: 0; right: 0; top: 563px; text-align: center;
    font-size: 18.5px; line-height: 31px; text-transform: uppercase; color: var(--ink);
  }
  .signatory { position: absolute; top: 710px; width: 202px; text-align: center; border-top: 1.5px solid #3a3a3a; padding-top: 10px; }
  .signatory--left { left: 261px; }
  .signatory--right { left: 759px; }
  .signatory-name { font-weight: 700; font-size: 17px; color: #111; }
  .signatory-role { font-size: 14px; color: #333; }
  .seal { position: absolute; left: 526px; top: 633px; width: 148px; height: 148px; }
  .footer {
    position: absolute; left: 0; top: 826px; width: 1200px; height: 114px;
    background: var(--band); color: #fff; text-align: center;
    font-family: "Open Sans", sans-serif; font-size: 15.5px; line-height: 22px; padding-top: 14px;
  }
  .footer-company { font-family: "Montserrat", sans-serif; font-weight: 900; font-size: 16px; letter-spacing: 0.5px; }
</style>
</head>
<body>
<main class="certificate">
  <svg class="corner-art" viewBox="0 0 420 660" role="img" aria-label="Decorative blue molecular network pattern">
    <defs>
      <radialGradient id="cornerGlow" cx="0.15" cy="0.2" r="0.85">
        <stop offset="0" stop-color="var(--blue-deep)" stop-opacity="0.85"/>
        <stop offset="0.55" stop-color="var(--blue-bright)" stop-opacity="0.35"/>
        <stop offset="1" stop-color="var(--blue-bright)" stop-opacity="0"/>
      </radialGradient>
    </defs>
    <rect width="420" height="660" fill="url(#cornerGlow)"/>
  </svg>

  <div class="brand"><span class="brand-dot"></span>TBM</div>

  <h1 class="title">CERTIFICATE</h1>
  <p class="subtitle">OF ACHIEVEMENT</p>

  <svg class="ribbon" viewBox="0 0 571 52" aria-hidden="true">
    <polygon points="0,14 60,14 60,52 0,52 18,33" fill="var(--ribbon-tail)"/>
    <polygon points="571,14 511,14 511,52 571,52 553,33" fill="var(--ribbon-tail)"/>
    <polygon points="45,46 45,52 55,46" fill="#0c2a42"/>
    <polygon points="526,46 526,52 516,46" fill="#0c2a42"/>
    <rect x="45" y="0" width="481" height="46" fill="var(--ribbon)"/>
  </svg>
  <p class="ribbon-text">This Certificate is Proudly Presented to</p>

  <p class="recipient">Marco Delgado</p>
  <div class="recipient-line"></div>

  <p class="details">
    Has completed the Fasciatherapy Level I course - 3 days, 15 - 17 February 2020<br>
    Kópavogur, Iceland 17 February 2020.
  </p>

  <div class="signatory signatory--left">
    <p class="signatory-name">Mr. JB van Dalen</p>
    <p class="signatory-role">Co-Director</p>
  </div>

  <svg class="seal" viewBox="0 0 148 148" aria-label="Registration number 1 ICE 20">
    <defs>
      <radialGradient id="silver" cx="0.4" cy="0.35" r="0.7">
        <stop offset="0" stop-color="var(--silver-light)"/>
        <stop offset="1" stop-color="var(--silver-dark)"/>
      </radialGradient>
    </defs>
    <circle cx="74" cy="74" r="72" fill="var(--ribbon)" stroke="var(--ribbon)" stroke-width="3" stroke-dasharray="4 3"/>
    <circle cx="74" cy="74" r="63" fill="url(#silver)" stroke="#ffffff" stroke-width="2"/>
    <circle cx="74" cy="74" r="57" fill="none" stroke="var(--ribbon)" stroke-width="1" stroke-dasharray="2 2"/>
    <g font-family="Montserrat, sans-serif" fill="var(--navy)" text-anchor="middle">
      <text x="74" y="57" font-size="10" font-weight="700">REGISTRATION</text>
      <text x="74" y="70" font-size="10" font-weight="700">NUMBER</text>
      <text x="74" y="92" font-size="19" font-weight="900">1 ICE 20</text>
    </g>
  </svg>

  <div class="signatory signatory--right">
    <p class="signatory-name">Mr. RT Hamid</p>
    <p class="signatory-role">Co-Director</p>
  </div>

  <footer class="footer">
    <p>The Tissue Balance Method ongoing certification is contingent upon meeting the requirements of the maintenance of the certification of Fasciatherapy</p>
    <p class="footer-company">TISSUELINE BV</p>
    <p>Havenstraat 14, 1011AB Amsterdam, The Netherlands</p>
    <p>Specialists in Fasciatherapy Innovation</p>
  </footer>
</main>
</body>
</html>
```